Design a New Site for a very cool Watch

We have the overall design element of the website and the banners in the PSD file. We need someone to finish our design in PSD and than convert to HTML. We have included the instructions, PSD file, images and all text.

We currently use Hubspot to host and make changes to our site. The entire design aspect is complete so all we need is some minor changes and additions within the photoshop design and than the coding into HTML.

Please only sign up if you understand photoshop and HTML conversion

Here is the DropBox link to the files
https://files.quorvel-share.net/s/pm4kx82lwq7dtne/Belthor%20Site.zip
Updates

We have the basic design concept in Photoshop.  We just need someone who can complete some changes, make some additions and convert to HTML

Target Market(s)

Watch Buyers

Requirements
Must have
• Must look like a professional luxury brand

Our brand colors are very basic with Black, White and Grey can be used

```html
<!DOCTYPE html>
<html lang="en">
<head>
<meta charset="utf-8">
<title>Belthor &amp; Co. — The Lyra Watch Collection</title>
<link rel="stylesheet" href="https://fonts.googleapis.com/css2?family=Marcellus&family=Arimo:wght@400&display=swap">
<style>
  :root {
    --page-bg: #ebebeb;
    --ink: #1a1a1a;
    --bar: #343434;
    --bar-rule: #d8d8d8;
    --white: #ffffff;
    --hero-black: #030303;
    --label-bg: rgba(40, 40, 40, 0.88);
    --tile-border: #d0d0d0;
    --social: #111111;
  }
  * { box-sizing: border-box; margin: 0; padding: 0; }
  html, body { width: 1200px; height: 937px; overflow: hidden; }
  body {
    background: var(--page-bg);
    position: relative;
    font-family: "Arimo", Arial, sans-serif;
    color: var(--ink);
  }

  /* Header */
  .site-header {
    position: absolute; left: 160px; top: 79px;
    width: 880px; height: 56px; display: flex;
  }
  .brand {
    width: 300px; height: 56px; background: var(--white);
    border: 1px solid var(--bar);
    display: flex; align-items: center; padding-left: 16px;
  }
  .brand-mark { width: 30px; height: 30px; background: var(--ink); }
  .brand-rule { width: 1px; height: 44px; background: var(--ink); margin: 0 16px 0 14px; }
  .brand-name {
    font-family: "Marcellus", serif; font-size: 27px; color: var(--ink);
    letter-spacing: 0.5px; white-space: nowrap;
  }
  .main-nav {
    flex: 1; background: var(--bar); display: flex; align-items: center;
    padding: 0 0 0 14px;
  }
  .main-nav a {
    font-family: "Marcellus", serif; font-size: 20px; color: var(--white);
    text-decoration: none; padding: 0 11px; height: 42px; line-height: 42px;
    border-right: 1px solid var(--bar-rule);
  }
  .main-nav a:last-child { border-right: 0; }

  /* Hero */
  .hero {
    position: absolute; left: 161px; top: 151px; width: 881px; height: 375px;
    background: var(--hero-black);
    box-shadow: 0 14px 16px -8px rgba(0,0,0,0.35);
  }
  .hero-product {
    position: absolute; left: 100px; top: 50px; width: 270px; height: 300px;
    background: radial-gradient(ellipse at 50% 45%, #c8141a 0%, #5a0a0c 45%, #030303 72%);
  }
  .hero-space {
    position: absolute; left: 397px; top: 26px; width: 484px; height: 349px;
    background: radial-gradient(ellipse at 45% 55%, #b5521c 0%, #5a1e0c 30%, #2a0c06 60%, #120604 100%);
  }
  .hero-copy { position: absolute; left: 452px; top: 96px; color: var(--white); }
  .hero-title { font-family: "Marcellus", serif; font-size: 27px; font-weight: 400; line-height: 1.1; }
  .hero-subtitle { font-size: 21px; margin-top: 2px; }
  .hero-text { font-size: 17px; line-height: 17px; margin-top: 12px; }
  .hero-note { font-size: 17px; margin-top: 18px; }
  .slide-arrow {
    position: absolute; top: 159px; width: 44px; height: 44px; border-radius: 50%;
    background: var(--white); display: flex; align-items: center; justify-content: center;
  }
  .slide-arrow.prev { left: -22px; }
  .slide-arrow.next { right: -22px; }

  /* Feature tiles */
  .feature-tiles {
    position: absolute; left: 160px; top: 574px; width: 882px; height: 188px;
    display: flex; gap: 17px;
  }
  .tile {
    position: relative; flex: 1; background: var(--white);
    border: 1px solid var(--tile-border);
    box-shadow: 0 8px 10px -6px rgba(0,0,0,0.3);
  }
  .tile-media { position: absolute; inset: 0; }
  .tile-media.story { background: linear-gradient(90deg, #f4f4f4 0%, #d6d6d6 55%, #6e6e6e 75%, #e8e8e8 100%); }
  .tile-media.register { background: linear-gradient(135deg, #7d8a94 0%, #c9b39a 45%, #e3d5c6 65%, #4a4a4a 100%); }
  .tile-media.warranty { background: linear-gradient(160deg, #cfcfd9 0%, #f2f2f2 40%, #e5e5e5 100%); }
  .tile-media.news { background: linear-gradient(180deg, #ffffff 0%, #2b2b2b 30%, #7fa8c8 45%, #e0e0e0 70%, #1c1c1c 100%); }
  .tile-label {
    position: absolute; left: 9px; right: 9px; bottom: 8px; height: 42px;
    background: var(--label-bg); color: var(--white);
    display: flex; align-items: center; justify-content: center; text-align: center;
    font-size: 17px; line-height: 16px;
  }

  /* Footer */
  .site-footer { position: absolute; left: 162px; top: 797px; font-size: 14px; line-height: 17px; }
  .site-footer a { color: var(--ink); text-decoration: none; }
  .social-links { position: absolute; left: 836px; top: 793px; display: flex; gap: 15px; }
  .social-links a { width: 41px; height: 41px; background: var(--social); display: block; }
</style>
</head>
<body>
  <header class="site-header">
    <div class="brand">
      <span class="brand-mark"></span>
      <span class="brand-rule"></span>
      <span class="brand-name">BELTHOR &amp; CO.</span>
    </div>
    <nav class="main-nav">
      <a href="#">about</a>
      <a href="#">collections</a>
      <a href="#">lifestyle</a>
      <a href="#">media</a>
      <a href="#">shop now</a>
      <a href="#">contact</a>
    </nav>
  </header>

  <section class="hero">
    <div class="hero-product" role="img" aria-label="Square watch with red dial and red strap on a black reflective surface"></div>
    <div class="hero-space" role="img" aria-label="Glowing orange galaxy in deep space"></div>
    <div class="hero-copy">
      <h1 class="hero-title">Time &amp; Space Fused Together</h1>
      <p class="hero-subtitle">The Lyra Watch Collection</p>
      <p class="hero-text">World's first watch with a piece of the Moon,<br>mars and a rare space gen set underneath<br>floating diamonds.</p>
      <p class="hero-note">Entire collection limited to 600 pices!</p>
    </div>
    <a class="slide-arrow prev" href="#" aria-label="Previous slide">
      <svg width="12" height="12" viewBox="0 0 12 12"><path d="M2 6 L10 1 L10 11 Z" fill="#111"/></svg>
    </a>
    <a class="slide-arrow next" href="#" aria-label="Next slide">
      <svg width="12" height="12" viewBox="0 0 12 12"><path d="M10 6 L2 1 L2 11 Z" fill="#111"/></svg>
    </a>
  </section>

  <section class="feature-tiles">
    <a class="tile" href="#">
      <div class="tile-media story" role="img" aria-label="Close-up of a watch dial and crown with floating diamonds"></div>
      <span class="tile-label">The Lyra Story</span>
    </a>
    <a class="tile" href="#">
      <div class="tile-media register" role="img" aria-label="Hand holding a pen over paperwork"></div>
      <span class="tile-label">Register your watch</span>
    </a>
    <a class="tile" href="#">
      <div class="tile-media warranty" role="img" aria-label="Warranty certificate held in a hand"></div>
      <span class="tile-label">Repair, warranty<br>&amp; maintenance</span>
    </a>
    <a class="tile" href="#">
      <div class="tile-media news" role="img" aria-label="Tablet and phone showing a news page"></div>
      <span class="tile-label">Subscribe &amp; find out<br>about new collections</span>
    </a>
  </section>

  <footer class="site-footer">
    <p><a href="#">Terms</a> | <a href="#">Disclaimer</a> | <a href="#">Privacy</a> | <a href="#">Questions</a> | <a href="#">Refund Poliies</a> &nbsp;| &nbsp;<a href="#">Contact</a></p>
    <p>Copyright © 2013. &nbsp;Belthor &amp; Co</p>
  </footer>
  <nav class="social-links" aria-label="Social links">
    <a href="#" aria-label="Pinora"></a>
    <a href="#" aria-label="Reelcast"></a>
    <a href="#" aria-label="Quipster"></a>
    <a href="#" aria-label="Circlebook"></a>
  </nav>
</body>
</html>
```